COMMERCIAL DOOR REPAIR
BUSINESS CARDS, LETTERHEAD, ENVELOPES, FAX COVER, EMAIL SIGNATURE
Rob Whitfield
NFPEI Certified Door Inspector
1752 E Pinnell Ln Glendale, AZ 85317
service@robsgatefix.com
www.robsgatefix.com
ROC# 514037
Not sure if font in logo can be used - open to other fonts as well. just no script or femine fonts. Not sure if all items on back will fit - open to re-wording, suggestions, etc.
24 Hour Emergency Services Available Specializing in: Automatic Doors Manual Doors Vitrelon Glass Doors Hollow Metal Doors Revolving Doors Also specializing in: Glass Mirrors Locksmithing Shower Doors Roof Hatches Re-seals Board-Ups

```html
<!DOCTYPE html>
<html lang="en">
<head>
<meta charset="utf-8">
<title>Rob's Gate Fix – Stationery Set</title>
<link rel="stylesheet" href="https://fonts.googleapis.com/css2?family=Roboto:wght@400;700&display=swap">
<style>
:root{
  --bg:#e9e6e1;
  --paper:#ffffff;
  --blue:#1b6fc2;
  --blue-dark:#0f4f93;
  --red:#c81e2b;
  --red-dark:#92121c;
  --ink:#3a3f47;
  --muted:#7c828b;
}
*{box-sizing:border-box;margin:0;padding:0}
html,body{width:1200px;height:794px;overflow:hidden}
body{background:var(--bg);font-family:"Roboto",Arial,sans-serif;color:var(--ink);position:relative}
.piece{position:absolute;background:var(--paper);box-shadow:0 3px 10px rgba(0,0,0,.22);overflow:hidden}

/* company name lockup: one colour, one weight, one plain circle */
.brand{display:flex;align-items:center;gap:7px;white-space:nowrap}
.brand-dot{flex:none;border-radius:50%;background:var(--ink)}
.brand-name{font-weight:700;color:var(--ink);line-height:1}
.brand-lg .brand-dot{width:14px;height:14px}
.brand-lg .brand-name{font-size:18px}
.brand-sm .brand-dot{width:10px;height:10px}
.brand-sm .brand-name{font-size:12px}

.small{font-size:6.5px;line-height:1.45;color:var(--muted)}

/* business card fronts */
.card{left:12px;width:308px;height:168px}
.card-front{border-top:5px solid var(--blue)}
.card-front .brand{position:absolute;left:14px;top:16px}
.card-front .address{position:absolute;left:14px;top:64px}
.card-front .person{position:absolute;left:160px;top:64px}
.person-name{font-size:11px;font-weight:700;color:var(--blue)}
.person-title{font-size:6.5px;color:var(--muted)}
.card-front .license{position:absolute;right:14px;bottom:10px}
.card-front .accent{position:absolute;left:0;bottom:0;width:100%;height:3px;background:var(--red)}

/* card backs */
.card-back{color:#fff;padding:12px 16px}
.card-blue{background:linear-gradient(160deg,var(--blue),var(--blue-dark))}
.card-red{background:linear-gradient(160deg,var(--red),var(--red-dark))}
.back-head{font-size:11px;font-weight:700;margin-bottom:10px}
.lists{display:flex;justify-content:space-between}
.list h4{font-size:7px;font-weight:700;margin-bottom:3px}
.list ul{list-style:none;font-size:6.5px;line-height:1.45}
.list ul li::before{content:"- "}
.card-red .brand-band{background:#fff;height:30px;margin:0 -16px 8px;padding:0 16px;display:flex;align-items:center}
.card-red .back-head{margin-bottom:6px}

/* sheets */
.sheet-top{left:341px;top:43px;width:391px;height:312px}
.sheet-main{left:341px;top:372px;width:391px;height:408px}
.sheet-right{left:749px;top:372px;width:441px;height:408px}
.sheet .rule{position:absolute;left:14px;top:52px;bottom:24px;width:2px;background:var(--blue)}
.sheet .rule::after{content:"";position:absolute;left:3px;top:0;bottom:0;width:1px;background:var(--red)}
.sheet .brand{position:absolute;left:14px;top:20px}
.sheet .contact{position:absolute;right:16px;top:16px;text-align:right}
.sheet .footer{position:absolute;left:24px;right:16px;bottom:8px;display:flex;justify-content:space-between;align-items:flex-end;border-top:1px solid #dfe3e8;padding-top:4px}
.sheet-right .return{position:absolute;left:200px;top:18px}
.sheet-right .license{position:absolute;right:16px;top:20px}

/* envelope back */
.envelope{left:749px;top:43px;width:441px;height:312px;border-top:4px solid var(--red)}
.envelope svg{position:absolute;left:0;top:0}
</style>
</head>
<body>

<section class="piece card card-front" style="top:48px">
  <div class="brand brand-sm"><span class="brand-dot"></span><span class="brand-name">Rob's Gate Fix</span></div>
  <div class="address small">1752 E Pinnell Ln<br>Glendale, AZ 85317<br><br>P 602.555.0148<br>F 602.555.0149<br>C 602.555.0150<br>service@robsgatefix.com<br>www.robsgatefix.com</div>
  <div class="person"><div class="person-name">Rob Whitfield</div><div class="person-title">NFPEI Certified Door Inspector</div></div>
  <div class="license small">License #: ROC 514037</div>
  <div class="accent"></div>
</section>

<section class="piece card card-front" style="top:233px">
  <div class="brand brand-sm"><span class="brand-dot"></span><span class="brand-name">Rob's Gate Fix</span></div>
  <div class="address small">1752 E Pinnell Ln<br>Glendale, AZ 85317<br><br>P 602.555.0148<br>F 602.555.0149<br>C 602.555.0150<br>service@robsgatefix.com<br>www.robsgatefix.com</div>
  <div class="person"><div class="person-name">Rob Whitfield</div><div class="person-title">NFPEI Certified Door Inspector</div></div>
  <div class="license small">License #: ROC 514037</div>
  <div class="accent"></div>
</section>

<section class="piece card card-back card-blue" style="top:415px">
  <div class="back-head">24 Hour Emergency Services Available</div>
  <div class="lists">
    <div class="list"><h4>Specializing in:</h4><ul><li>Automatic Doors</li><li>Manual Doors</li><li>Vitrelon Glass Doors</li><li>Hollow Metal Doors</li><li>Revolving Doors</li></ul></div>
    <div class="list"><h4>Also specializing in:</h4><ul><li>Glass</li><li>Mirrors</li><li>Locksmithing</li><li>Shower Doors</li><li>Roof Hatches</li><li>Re-seals</li><li>Board-Ups</li></ul></div>
  </div>
</section>

<section class="piece card card-back card-red" style="top:600px;padding-top:0">
  <div class="brand-band"><div class="brand brand-sm"><span class="brand-dot"></span><span class="brand-name">Rob's Gate Fix</span></div></div>
  <div class="back-head">24 Hour Emergency Services Available</div>
  <div class="lists">
    <div class="list"><h4>Specializing in:</h4><ul><li>Automatic Doors</li><li>Manual Doors</li><li>Vitrelon Glass Doors</li><li>Hollow Metal Doors</li><li>Revolving Doors</li></ul></div>
    <div class="list"><h4>Also specializing in:</h4><ul><li>Glass</li><li>Mirrors</li><li>Locksmithing</li><li>Shower Doors</li><li>Roof Hatches</li><li>Re-seals</li><li>Board-Ups</li></ul></div>
  </div>
</section>

<section class="piece sheet sheet-top">
  <div class="brand brand-lg"><span class="brand-dot"></span><span class="brand-name">Rob's Gate Fix</span></div>
  <div class="rule"></div>
  <div class="contact small">www.robsgatefix.com<br>P 602.555.0148 | F 602.555.0149<br>service@robsgatefix.com</div>
  <div class="footer small"><span>1752 E Pinnell Ln, Glendale, AZ 85317</span><span>License #: ROC 514037</span></div>
</section>

<section class="piece envelope">
  <svg width="441" height="308" viewBox="0 0 441 308">
    <path d="M0 0H441V40L236 118Q220 124 205 118L0 40Z" fill="var(--blue)"/>
    <path d="M0 40L205 118Q220 124 236 118L441 40" fill="none" stroke="var(--blue-dark)" stroke-width="2"/>
  </svg>
</section>

<section class="piece sheet sheet-main">
  <div class="brand brand-lg"><span class="brand-dot"></span><span class="brand-name">Rob's Gate Fix</span></div>
  <div class="rule"></div>
  <div class="footer small"><span>1752 E Pinnell Ln, Glendale, AZ 85317 &nbsp;|&nbsp; P 602.555.0148 &nbsp;|&nbsp; F 602.555.0149</span><span style="text-align:right">www.robsgatefix.com<br>License #: ROC 514037</span></div>
</section>

<section class="piece sheet sheet-right">
  <div class="brand brand-lg"><span class="brand-dot"></span><span class="brand-name">Rob's Gate Fix</span></div>
  <div class="return small">1752 E Pinnell Ln, Glendale, AZ 85317<br>P 602.555.0148 | F 602.555.0149<br>www.robsgatefix.com<br>service@robsgatefix.com</div>
  <div class="license small">License #: ROC 514037</div>
</section>

</body>
</html>
```